Job Coaching - Mova; engaging people to improve their work experience

design a website focussed on people
with 4 tabs/pages (+2)
1) landing page
2) Professional
3) Job Coaching
4) Bio
5) Contact
6) references

I've added the text to be used in the documents. The website will be in Dutch, but I've added the translations in green just for you to understand what it is about.

I've added my logo as well, and a flyer I used already. this gives you an idea on how it could look like
Pictures you can find there as well. Other pictures can be added of course
The techical creation of the website is not needed. I need all the designs and information to be able to create it myself.

```html
<!DOCTYPE html>
<html lang="nl">
<head>
<meta charset="utf-8">
<title>Mova – Job Coaching</title>
<link rel="stylesheet" href="https://fonts.googleapis.com/css2?family=Oswald:wght@300;400;500;600;700&family=Poppins:wght@400;500;600&display=swap">
<style>
  :root{
    --teal:#3aa99f;
    --teal-dark:#2e8f86;
    --graphite:#616161;
    --ink:#555555;
    --text:#333333;
    --mist:#ececec;
    --mint:#eef5f3;
    --white:#ffffff;
    --sky-a:#1aa6cf;
    --sky-b:#137d9e;
    --sky-c:#0f3a4a;
  }
  *{box-sizing:border-box;margin:0;padding:0}
  html,body{width:1200px;height:2895px;overflow:hidden;background:var(--white)}
  .page{position:relative;width:1200px;height:2895px;overflow:hidden;font-family:'Poppins',sans-serif;color:var(--text)}
  .abs{position:absolute}

  /* header */
  .site-header{position:absolute;left:0;top:0;width:1200px;height:68px;background:var(--white);z-index:5}
  .brand{position:absolute;left:101px;top:12px;display:flex;align-items:center;gap:10px}
  .brand-dot{width:34px;height:34px;border-radius:50%;background:var(--teal)}
  .brand-name{font-family:'Oswald',sans-serif;font-weight:500;font-size:36px;line-height:1;color:var(--teal);letter-spacing:1px}
  .main-nav{position:absolute;left:348px;top:25px;display:flex;align-items:center;gap:20px;font-size:14px;font-weight:500;color:var(--ink)}
  .nav-home{width:16px;height:14px}
  .nav-cta{position:absolute;left:892px;top:12px;width:219px;height:44px;background:var(--teal);color:var(--white);font-size:14px;font-weight:600;display:flex;align-items:center;justify-content:center}

  /* hero */
  .hero-photo{left:0;top:68px;width:1200px;height:1044px;background:radial-gradient(ellipse at 35% 60%,var(--sky-a) 0%,var(--sky-b) 55%,var(--sky-c) 100%)}
  .shapes{left:0;top:0;width:1200px;height:2895px}
  .hero-welcome{left:88px;top:196px;font-family:'Oswald',sans-serif;font-weight:400;font-size:46px;line-height:1;color:var(--white);display:flex;align-items:center;gap:24px}
  .hero-welcome::after{content:"";display:block;width:224px;height:3px;background:rgba(255,255,255,.35)}
  .hero-job{left:82px;top:236px;font-family:'Oswald',sans-serif;font-weight:700;font-size:150px;line-height:1;color:var(--white)}
  .hero-coaching{left:78px;top:374px;font-family:'Oswald',sans-serif;font-weight:300;font-size:128px;line-height:1;color:var(--white)}
  .hero-tagline{left:88px;top:520px;font-family:'Oswald',sans-serif;font-weight:400;font-size:22px;color:var(--white)}
  .hero-btn{left:90px;top:575px;width:222px;height:45px;background:var(--white);color:var(--text);font-size:14px;font-weight:600;display:flex;align-items:center;justify-content:center}
  .intro-text{left:848px;top:836px;width:312px;text-align:center;font-family:'Oswald',sans-serif;font-weight:500;font-size:38px;line-height:44.6px;color:var(--white);text-transform:uppercase}

  /* about */
  .about-title{left:91px;top:1646px;font-family:'Oswald',sans-serif;font-weight:600;font-size:40px;line-height:1.1;color:var(--ink)}
  .about-title span,.partner-title span{color:var(--teal)}
  .about-text{left:91px;top:1698px;width:505px;font-size:14px;line-height:20.5px;color:var(--text)}
  .about-mark{left:640px;top:1640px;width:460px;height:360px;display:flex;align-items:center;justify-content:center;gap:26px}
  .about-mark .mark-dot{width:90px;height:90px;border-radius:50%;background:var(--teal)}
  .about-mark .mark-name{font-family:'Oswald',sans-serif;font-weight:600;font-size:140px;line-height:1;color:var(--graphite)}

  /* partners */
  .partner-title{left:124px;top:2146px;width:470px;font-family:'Oswald',sans-serif;font-weight:600;font-size:39px;line-height:40px;color:var(--ink);text-transform:uppercase}

  /* footer */
  .footer-brand{left:0;top:2540px;width:1200px;display:flex;justify-content:center;align-items:center;gap:16px}
  .footer-brand .brand-dot{width:60px;height:60px;background:var(--white)}
  .footer-brand .brand-name{color:var(--white);font-size:70px}
  .contact-item{top:2686px;display:flex;align-items:flex-start}
  .contact-label{font-family:'Oswald',sans-serif;font-size:13px;color:var(--white);line-height:1.2}
  .contact-value{font-size:16px;color:var(--white);line-height:1.4}
  .footer-rule{left:90px;top:2831px;width:1022px;height:1px;background:rgba(255,255,255,.3)}
  .copyright{left:0;top:2851px;width:1200px;text-align:center;font-family:'Oswald',sans-serif;font-size:16px;color:var(--white)}
</style>
</head>
<body>
<div class="page">

  <div class="abs hero-photo" role="img" aria-label="Photo: wooden figure climbing wooden steps held by a hand, on a blue backdrop"></div>

  <svg class="abs shapes" viewBox="0 0 1200 2895" aria-hidden="true">
    <!-- soft background triangles -->
    <polygon points="0,1945 470,2360 0,2480" fill="var(--mint)"/>
    <polygon points="1200,2376 1010,2570 1200,2570" fill="var(--mist)"/>
    <!-- hero teal wedge and grey diamond -->
    <polygon points="1200,376 607,966 1200,1562" fill="var(--teal)"/>
    <polygon points="748,1112 969,1337 748,1556 528,1337" fill="var(--mist)"/>
    <!-- partner badges -->
    <polygon points="726,2107 835,2216 726,2325 617,2216" fill="var(--mist)"/>
    <polygon points="966,2107 1075,2216 966,2325 857,2216" fill="var(--mist)"/>
    <rect x="704" y="2192" width="44" height="44" rx="6" fill="#5a3f8c"/>
    <rect x="905" y="2198" width="126" height="36" rx="3" fill="#17336b"/>
    <!-- footer band -->
    <polygon points="0,2650 596,2378 1200,2665 1200,2895 0,2895" fill="var(--teal)"/>
    <polygon points="0,2665 596,2398 1200,2680 1200,2895 0,2895" fill="var(--graphite)"/>
    <!-- contact icon frames -->
    <g fill="none" stroke="rgba(255,255,255,.35)" stroke-width="1.5">
      <polygon points="255,2673 290,2708 255,2743 220,2708"/>
      <polygon points="554,2673 589,2708 554,2743 519,2708"/>
      <polygon points="805,2673 840,2708 805,2743 770,2708"/>
    </g>
    <!-- globe -->
    <g fill="none" stroke="var(--white)" stroke-width="2">
      <circle cx="255" cy="2708" r="10"/>
      <ellipse cx="255" cy="2708" rx="4" ry="10"/>
      <line x1="245" y1="2708" x2="265" y2="2708"/>
    </g>
    <!-- phone -->
    <path d="M547 2699 l5-3 4 7-3 2 q2 5 7 7 l2-3 7 4-3 5 q-14 1-19-19z" fill="var(--white)"/>
    <!-- envelope -->
    <rect x="795" y="2701" width="20" height="14" fill="var(--white)"/>
    <polyline points="795,2702 805,2710 815,2702" fill="none" stroke="var(--graphite)" stroke-width="1.5"/>
    <!-- back to top -->
    <polygon points="1154,2806 1179,2831 1154,2856 1129,2831" fill="var(--teal)"/>
    <path d="M1154 2840 v-16 M1149 2829 l5-5 5 5" stroke="var(--white)" stroke-width="1.5" fill="none"/>
  </svg>

  <svg class="abs" style="left:0;top:0" width="1200" height="1600" viewBox="0 0 1200 1600" role="img" aria-label="Portrait photo of the coach smiling, in a red shirt">
    <defs>
      <linearGradient id="portraitTone" x1="0" y1="0" x2="0" y2="1">
        <stop offset="0" stop-color="#a48266"/>
        <stop offset=".5" stop-color="#9a5c4c"/>
        <stop offset="1" stop-color="#7a2a36"/>
      </linearGradient>
    </defs>
    <polygon points="307,671 748,1112 307,1554 -134,1112" fill="url(#portraitTone)"/>
  </svg>

  <header class="site-header">
    <div class="brand"><span class="brand-dot"></span><span class="brand-name">MOVA</span></div>
    <nav class="main-nav">
      <svg class="nav-home" viewBox="0 0 16 14" aria-label="Home"><path d="M8 0 L16 7 H13 V14 H10 V9 H6 V14 H3 V7 H0 Z" fill="var(--teal)"/></svg>
      <span>PROFESSIONAL</span><span>JOB COACHING</span><span>BIO</span><span>CONTACT</span><span>REFERENCES</span>
    </nav>
    <div class="nav-cta">MET LOOPBAANCHEQUES</div>
  </header>

  <div class="abs hero-welcome">WELCOME TO</div>
  <div class="abs hero-job">JOB</div>
  <div class="abs hero-coaching">COACHING</div>
  <div class="abs hero-tagline">ONTDEK DE KRACHT VAN AUTHENTIEK LEIDERSCHAP</div>
  <div class="abs hero-btn">MET LOOPBAANCHEQUES</div>
  <p class="abs intro-text">Hallo, ik ben Tom Verbeke. Als gepassioneerd loopbaancoach wil ik jou in je kracht zetten bij het uitoefenen van je job, elke dag opnieuw</p>

  <h2 class="abs about-title">ABOUT <span>TOM VERBEKE</span></h2>
  <p class="abs about-text">We blijven steeds langer aan de slag en daarom is het vandaag meer dan ooit belangrijk om de nodige aandacht te besteden aan professionele groei en welzijn op het werk.<br>Ik ben ervan overtuigd dat mensen vaak tot meer in staat zijn dan ze zelf geloven. Alles begint met het verlangen naar verandering. Wie ben ik? Wat is mijn rol? Wat wil ik écht?<br>Als jobcoach ga ik niet voor eenvoudige quick-wins of kant-en-klare tips en tricks. In een geest van openheid, vertrouwen en gelijkwaardigheid gaan we samen op zoek naar de diepere inzichten en duurzame oplossingen die voor jou werken. Coaching is een bewustwordingsproces dat leidt tot het vinden van de antwoorden in jezelf.<br>Meld je vandaag nog aan voor een vrijblijvend kennismakingsgesprek en neem de regie van je loopbaan (opnieuw) in handen.</p>
  <div class="abs about-mark"><span class="mark-dot"></span><span class="mark-name">MOVA</span></div>

  <h2 class="abs partner-title">In samenwerking <span>met het Loopbaanhuis</span> - via de loopbaancheques van Werkpunt</h2>

  <div class="abs footer-brand"><span class="brand-dot"></span><span class="brand-name">MOVA</span></div>

  <div class="abs contact-item" style="left:298px"><div><div class="contact-label">DOMAIN*</div><div class="contact-value">www.movacoaching.be</div></div></div>
  <div class="abs contact-item" style="left:595px"><div><div class="contact-label">CALL US*</div><div class="contact-value">0470/318452;</div></div></div>
  <div class="abs contact-item" style="left:847px;top:2682px"><div><div class="contact-label">EMAIL US*</div><div class="contact-value">tom.verbeke@movacoaching.be</div></div></div>

  <div class="abs footer-rule"></div>
  <div class="abs copyright">© COPYRIGHT 2023 | ALL RIGHTS RESERVED</div>
</div>
</body>
</html>
```